Recommend a friend FLYER - Brisk Window Cleaning

Window cleaning company with focus on quality of service and professionalism. Friendly, relaxed tone, and simple clear communications.

Target Market(s)

Homeowners with moderate income

Industry/Entity Type

Window Cleaning

Font styles to use
Serif
Decorative

Colors
33a6d7
fbee3d
faa54b
d3d3d3

```html
<!DOCTYPE html>
<html lang="en">
<head>
<meta charset="utf-8">
<title>Refer a Friend Flyer – Brisk Window Cleaning</title>
<link rel="stylesheet" href="https://fonts.googleapis.com/css2?family=Open+Sans:ital,wght@0,400;0,600;0,700;1,400;1,600;1,700&family=Tinos:ital,wght@1,700&display=swap">
<style>
  :root {
    --sky: #33a6d7;
    --teal: #2a93b8;
    --teal-deep: #1d7fa3;
    --navy: #1f4a8f;
    --orange: #f7911f;
    --orange-soft: #faa54b;
    --yellow: #fbee3d;
    --grey: #d3d3d3;
    --field: #f2f2f2;
    --ink: #4d5a63;
    --white: #ffffff;
    --stage: #ececec;
  }
  * { box-sizing: border-box; margin: 0; padding: 0; }
  html, body { width: 1157px; height: 1200px; overflow: hidden; }
  body { background: var(--stage); font-family: "Open Sans", Arial, sans-serif; position: relative; }

  .flyer {
    position: absolute; width: 438px; height: 918px; overflow: hidden;
    box-shadow: 0 6px 18px rgba(0,0,0,.18);
  }
  .flyer--front { left: 78px; top: 98px; background: linear-gradient(#f4fbff, #e2f1f9 55%, #ffffff 80%); }
  .flyer--back { left: 603px; top: 187px; background: linear-gradient(var(--teal) 0%, #7ec3dc 40%, #cfe8f2 70%, #f3f9fc 88%); }

  .layer { position: absolute; left: 0; top: 0; }

  .front-title {
    position: absolute; top: 32px; width: 100%; text-align: center;
    font-weight: 700; font-size: 40px; letter-spacing: -0.5px; color: var(--orange);
  }

  .brand {
    position: absolute; left: 0; width: 100%;
    display: flex; align-items: center; justify-content: center; gap: 10px;
    font-weight: 700; font-size: 32px; color: var(--navy); letter-spacing: -0.5px;
  }
  .brand__mark { width: 30px; height: 30px; background: var(--sky); flex: none; }
  .flyer--front .brand { top: 528px; }
  .flyer--back .brand { top: 738px; font-size: 30px; }

  .offer { position: absolute; left: 76px; top: 592px; width: 290px; height: 210px; }
  .offer__intro { position: absolute; left: 50px; top: 30px; font-style: italic; font-weight: 600; font-size: 19px; color: #555; }
  .offer__amount { position: absolute; left: 38px; top: 50px; font-weight: 700; font-size: 58px; color: var(--orange); letter-spacing: -2px; line-height: 1.1; }
  .offer__note { position: absolute; left: 156px; top: 76px; font-weight: 700; font-size: 16px; letter-spacing: -0.3px; line-height: 1.2; color: #555; }

  .front-thanks { position: absolute; right: 24px; top: 826px; text-align: right; color: var(--white); }
  .front-thanks__main { font-style: italic; font-weight: 700; font-size: 26px; line-height: 1; }
  .front-thanks__sub { font-style: italic; font-size: 15px; margin-top: 2px; }
  .front-thanks__small { font-style: italic; font-size: 9px; margin-top: 6px; }

  .form { position: absolute; left: 22px; top: 0; width: 394px; }
  .form__heading { position: absolute; left: 4px; font-size: 15px; color: var(--white); }
  .field {
    position: absolute; left: 0; width: 394px; height: 36px;
    background: var(--field); padding: 0 10px; line-height: 36px;
    font-size: 14px; color: #6b6b6b;
  }

  .terms {
    position: absolute; left: 22px; width: 394px;
    font-size: 15px; line-height: 1.45; color: var(--ink);
  }
  .terms--justify { text-align: justify; }

  .back-thanks {
    position: absolute; top: 668px; width: 100%; text-align: center;
    font-family: "Tinos", "Times New Roman", serif; font-style: italic; font-weight: 700;
    font-size: 22px; color: var(--orange-soft);
  }

  .contact { position: absolute; right: 14px; top: 860px; text-align: right; color: var(--white); font-size: 15px; line-height: 1.45; }
  .contact__phone { display: flex; align-items: center; justify-content: flex-end; gap: 6px; }
</style>
</head>
<body>

<section class="flyer flyer--front">
  <svg class="layer" width="438" height="918" viewBox="0 0 438 918">
    <defs>
      <linearGradient id="bandBlue" x1="0" y1="0" x2="1" y2="0">
        <stop offset="0" stop-color="#2a8fb6"/>
        <stop offset="1" stop-color="#1f7ea6"/>
      </linearGradient>
      <linearGradient id="skyFill" x1="0" y1="0" x2="0" y2="1">
        <stop offset="0" stop-color="#4a86c8"/>
        <stop offset=".6" stop-color="#bfe0f4"/>
        <stop offset="1" stop-color="#e6f4fb"/>
      </linearGradient>
    </defs>
    <path d="M0 125 Q60 190 140 200 L438 200 L438 360 Q200 370 0 500 Z" fill="url(#bandBlue)"/>
    <path d="M0 500 Q160 385 438 370" stroke="#ffffff" stroke-width="8" fill="none"/>
    <path d="M0 514 Q170 400 438 384" stroke="#c9d2d8" stroke-width="6" fill="none"/>
    <path role="img" aria-label="Cartoon blue bird holding a megaphone beside an orange window squeegee, set against a blue sky with clouds"
          d="M40 150 Q120 110 300 115 Q380 120 438 175 L438 345 Q250 355 130 415 Q70 425 40 385 Z" fill="url(#skyFill)"/>
    <g transform="translate(76 592)">
      <ellipse cx="144" cy="80" rx="128" ry="70" fill="#ececec" stroke="var(--teal)" stroke-width="4"/>
      <path d="M175 146 L170 182 L205 140" fill="#ececec" stroke="var(--teal)" stroke-width="4" stroke-linejoin="round"/>
      <path d="M168 140 L206 138 L200 146 L170 148 Z" fill="#ececec"/>
    </g>
    <path d="M0 805 Q60 830 120 850 L0 880 Z" fill="var(--orange-soft)"/>
    <path d="M0 880 Q200 830 438 810 L438 918 L0 918 Z" fill="url(#bandBlue)"/>
    <path d="M0 880 Q200 830 438 810" stroke="#ffffff" stroke-width="4" fill="none"/>
  </svg>

  <h1 class="front-title">REFER A FRIEND TO</h1>

  <div class="brand"><span>Brisk Window Cleaning</span><span class="brand__mark"></span></div>

  <div class="offer">
    <span class="offer__intro">and get a</span>
    <span class="offer__amount">£10</span>
    <span class="offer__note">voucher<br>as a little</span>
  </div>

  <div class="front-thanks">
    <p class="front-thanks__main">Thank You</p>
    <p class="front-thanks__sub">from us!</p>
    <p class="front-thanks__small">See reverse for more details</p>
  </div>
</section>

<section class="flyer flyer--back">
  <div class="form">
    <p class="form__heading" style="top:20px">YOUR DETAILS:</p>
    <div class="field" style="top:54px">Name:</div>
    <div class="field" style="top:104px">Address:</div>
    <div class="field" style="top:143px"></div>
    <div class="field" style="top:182px"></div>

    <p class="form__heading" style="top:231px">YOUR FRIEND'S DETAILS:</p>
    <div class="field" style="top:266px">Name:</div>
    <div class="field" style="top:315px">Address:</div>
    <div class="field" style="top:354px"></div>
    <div class="field" style="top:393px"></div>
    <div class="field" style="top:446px">Telephone No:</div>
  </div>

  <p class="terms terms--justify" style="top:498px">You will receive a £10 voucher redeemable against any of our services, on completion of your friend's first clean. Must be within the areas we cover.</p>
  <p class="terms" style="top:588px">You will receive a voucher for each referral.<br>Recommend us to as many friends as you can!</p>

  <p class="back-thanks">Thank you for your loyal support</p>

  <div class="brand"><span>Brisk Window Cleaning</span><span class="brand__mark"></span></div>

  <svg class="layer" width="437" height="918" viewBox="0 0 437 918">
    <path d="M0 805 Q50 830 110 848 L0 870 Z" fill="var(--orange-soft)"/>
    <path d="M0 870 Q200 820 437 805 L437 918 L0 918 Z" fill="var(--teal)"/>
    <path d="M0 870 Q200 820 437 805" stroke="#ffffff" stroke-width="4" fill="none"/>
  </svg>

  <div class="contact">
    <p class="contact__phone">
      <svg width="18" height="18" viewBox="0 0 18 18" aria-hidden="true">
        <circle cx="9" cy="9" r="8" fill="none" stroke="#fff" stroke-width="1.4"/>
        <path d="M6 4.8 L7.6 6.8 L6.9 7.7 Q7.8 9.6 10 11 L10.9 10.3 L13 11.9 L12 13.2 Q8.5 13 5.3 8.5 Q4.8 6 6 4.8 Z" fill="#fff"/>
      </svg>
      0800 555 0142 • 01632 960418
    </p>
    <p>www.briskwindowcleaning.co.uk</p>
  </div>
</section>

</body>
</html>
```